Startup Drone Platform Company business card

We are needing a business card design for our employees. We are a startup drone platform. We are looking for a business card that has our logo on one side, with the employee/company details on the opposite side. We are looking for something that is very eye catching, modern, and bold.

Target Market(s)

This will target both drone pilots and drone businesses, along with all the industries that could utilize drone services (aerial video, aerial photos, inspections, 3d mapping, etc).

Industry/Entity Type

Business

```html
<!DOCTYPE html>
<html lang="en">
<head>
<meta charset="utf-8">
<title>Skyhire Aerial – Business Card</title>
<link rel="stylesheet" href="https://fonts.googleapis.com/css2?family=Arimo:wght@400&family=Libre+Baskerville:wght@400&family=Montserrat:wght@500&display=swap">
<style>
  :root {
    --teal: #2fa9b5;
    --teal-dark: #238c97;
    --ink: #3a3a3a;
    --muted: #7b7b7b;
    --paper: #ffffff;
    --paper-shade: #e9e9e9;
    --night: #0b0b0b;
    --backdrop: #2a2a2a;
  }
  * { margin: 0; padding: 0; box-sizing: border-box; }
  html, body { width: 1200px; height: 997px; overflow: hidden; }
  body {
    background: var(--backdrop);
    position: relative;
    font-family: "Arimo", Arial, sans-serif;
  }
  .card {
    position: absolute;
    width: 500px;
    height: 286px;
    border-radius: 16px;
    overflow: hidden;
  }
  .card--front {
    left: 80px; top: 356px;
    background: linear-gradient(135deg, var(--paper) 40%, var(--paper-shade) 100%);
  }
  .card--back {
    left: 620px; top: 356px;
    background: var(--night);
  }

  /* wordmark */
  .wordmark {
    position: absolute;
    display: flex;
    align-items: center;
    gap: 12px;
    font-family: "Montserrat", Arial, sans-serif;
    font-weight: 500;
  }
  .wordmark__dot {
    border-radius: 50%;
    background: var(--teal);
    flex: none;
  }
  .wordmark__text { display: flex; flex-direction: column; align-items: center; line-height: 1.1; }
  .wordmark__name { letter-spacing: 0.32em; }
  .wordmark__sub { letter-spacing: 0.4em; }

  .card--front .wordmark { right: 36px; top: 64px; color: var(--ink); }
  .card--front .wordmark__dot { width: 18px; height: 18px; }
  .card--front .wordmark__name { font-size: 22px; }
  .card--front .wordmark__sub { font-size: 11px; }

  .card--back .wordmark { left: 50%; top: 50%; transform: translate(-50%, -50%); color: #e8e8e8; }
  .card--back .wordmark__dot { width: 26px; height: 26px; }
  .card--back .wordmark__name { font-size: 32px; }
  .card--back .wordmark__sub { font-size: 14px; }

  /* person */
  .person { position: absolute; left: 34px; top: 112px; }
  .person__name {
    font-family: "Libre Baskerville", Georgia, serif;
    color: var(--teal);
    font-size: 19px;
  }
  .person__role { color: var(--muted); font-size: 12px; margin-top: 2px; }

  /* contact tab */
  .contact-tab {
    position: absolute;
    left: 0; bottom: 0;
    width: 40px; height: 92px;
    background: var(--teal);
    border-top-right-radius: 10px;
    display: flex; flex-direction: column;
    justify-content: space-around; align-items: center;
    padding: 8px 0;
  }
  .contact-tab svg { width: 12px; height: 12px; fill: #fff; }
  .contact-list {
    position: absolute;
    left: 52px; bottom: 12px;
    list-style: none;
    color: var(--ink);
    font-size: 11px;
    line-height: 1.35;
  }
  .contact-list li + li { margin-top: 6px; }

  /* email band */
  .email-band {
    position: absolute;
    right: 0; bottom: 0;
    height: 22px;
    padding: 0 14px 0 18px;
    background: var(--teal);
    border-top-left-radius: 11px;
    color: #fff;
    font-size: 10px;
    letter-spacing: 0.08em;
    display: flex; align-items: center;
  }
</style>
</head>
<body>
  <section class="card card--front" aria-label="Card front">
    <div class="wordmark">
      <span class="wordmark__dot"></span>
      <span class="wordmark__text">
        <span class="wordmark__name">SKYHIRE</span>
        <span class="wordmark__sub">AERIAL</span>
      </span>
    </div>

    <div class="person">
      <p class="person__name">Marco L Reyes</p>
      <p class="person__role">Managing Partner</p>
    </div>

    <div class="contact-tab">
      <svg viewBox="0 0 24 24" aria-hidden="true"><path d="M6.6 10.8a15.1 15.1 0 0 0 6.6 6.6l2.2-2.2a1 1 0 0 1 1-.25 11.4 11.4 0 0 0 3.6.57 1 1 0 0 1 1 1V20a1 1 0 0 1-1 1A17 17 0 0 1 3 4a1 1 0 0 1 1-1h3.5a1 1 0 0 1 1 1c0 1.25.2 2.45.57 3.57a1 1 0 0 1-.25 1z"/></svg>
      <svg viewBox="0 0 24 24" aria-hidden="true"><path d="M12 2a7 7 0 0 0-7 7c0 5.25 7 13 7 13s7-7.75 7-13a7 7 0 0 0-7-7zm0 9.5A2.5 2.5 0 1 1 12 6.5a2.5 2.5 0 0 1 0 5z"/></svg>
      <svg viewBox="0 0 24 24" aria-hidden="true"><path d="M12 2a7 7 0 0 0-7 7c0 5.25 7 13 7 13s7-7.75 7-13a7 7 0 0 0-7-7zm0 9.5A2.5 2.5 0 1 1 12 6.5a2.5 2.5 0 0 1 0 5z"/></svg>
    </div>

    <ul class="contact-list">
      <li>+1 (555) 014-2290</li>
      <li>Unit no 42, sec 17, Delhi</li>
      <li>18 Alder Grove Road, 2nd Floor,<br>Fairview, CT 06000</li>
    </ul>

    <div class="email-band">hello@skyhireaerial.com</div>
  </section>

  <section class="card card--back" aria-label="Card back">
    <div class="wordmark">
      <span class="wordmark__dot"></span>
      <span class="wordmark__text">
        <span class="wordmark__name">SKYHIRE</span>
        <span class="wordmark__sub">AERIAL</span>
      </span>
    </div>
  </section>
</body>
</html>
```